New webpage design for Talvora.se, participant management system informationpage.

Project Brief: New Website Design for Talvora.se (Participant Management System)
About Talvora.se:
Talvora.se is an established participant management system used by organizations and course providers in Sweden to handle event and course registrations. Our website’s primary audience is course providers, event organizers, and potential users seeking efficient management tools.
Project Goal:
We are launching a new public-facing website for Talvora.se, which will present information about our system, features, FAQ, pricing, news, testimonials, and more. The new site will be built in Umbraco CMS and should follow our visual identity as described in the attached graphic manual.
Deliverables:
We need complete, modern, and responsive page designs (desktop and mobile) for the following pages:
- Home page (landing page)
- Features page
- FAQ page
- About Us page
- Contact Us / Book a Demo page
- Pricing page
- Testimonials page
- News / Blog page
Design Guidelines:
- Please use the attached Plomvik graphic manual for guidance (Plomvik is a sister project; use the same branding).
- The Talvora.se logo is attached and must be included.
- Please use the blue color palette variant from the guide.
- Typography and graphic elements should be consistent with the manual.
- Designs must be suitable for implementation in Umbraco CMS (avoid overly complex layouts or animations that might be difficult to develop).
- All designs should be responsive and work well on desktop, tablet, and mobile.
- Final deliverables should be provided in Figma or Adobe XD (preferably Figma).
What We Like:
- Clean, modern, Scandinavian style.
- Clear navigation and strong hierarchy.
- Readable, accessible layouts.
What to Avoid:
- Overly playful or cartoonish elements.
- Too much clutter or excessive graphical elements.
- Dark color schemes (please focus on blue/light).
References:
- Our current site: https://talvora-demo.se
- Graphic manual (see attachment)
- Talvora logo (see attachment)
Additional Notes:
- The new design should improve clarity, usability, and visual appeal compared to our current site.
- Feel free to suggest visual improvements, but remain consistent with our brand guidelines.
Other font styles liked:
- Orev and Cabin. See attached font files

```html
<!DOCTYPE html>
<html lang="sv">
<head>
<meta charset="utf-8">
<title>Talvora – Hantera dina kurser, deltagare och betalningar</title>
<link href="https://fonts.googleapis.com/css2?family=Arimo:wght@400;700&family=Cabin:wght@400;500;600;700&display=swap" rel="stylesheet">
<style>
:root{
  --blue:#089fe6;
  --blue-dark:#0787c6;
  --sky:#a9dcf7;
  --sky-deep:#36b1ee;
  --notice:#c4e8fa;
  --ink:#1f2328;
  --muted:#5c6670;
  --soft:#f6f8fa;
  --card:#f7f9fb;
  --dark:#232323;
  --white:#fff;
  --green:#22c55e;
}
*{box-sizing:border-box;margin:0;padding:0}
html,body{width:1200px;height:3727px;overflow:hidden}
body{font-family:"Cabin",sans-serif;color:var(--ink);background:var(--white);font-size:14px}
h1,h2,h3,h4{font-family:"Arimo",sans-serif;font-weight:700}
.wrap{width:890px;margin:0 auto;position:relative}
section,header,footer{position:relative}
.btn{display:inline-block;font-family:"Cabin",sans-serif;font-weight:600;font-size:11px;border-radius:5px;padding:0 22px;height:32px;line-height:32px;text-decoration:none}
.btn-solid{background:var(--blue);color:var(--white)}
.btn-outline{border:1.5px solid var(--blue);color:var(--blue);background:var(--white)}
.center{text-align:center}

/* nav */
.site-nav{height:52px;background:var(--white);border-bottom:1px solid #e8edf1}
.site-nav .wrap{display:flex;align-items:center;height:52px}
.brand{font-family:"Cabin",sans-serif;font-weight:600;font-size:16px;color:var(--ink)}
.nav-links{display:flex;gap:27px;margin-left:125px;font-size:11px;color:#444}
.nav-links a{color:inherit;text-decoration:none}
.nav-login{margin-left:auto;height:30px;line-height:30px;padding:0 12px}

/* hero */
.hero{height:417px;background:linear-gradient(115deg,var(--sky) 0%,#7ccbf3 55%,var(--sky-deep) 100%)}
.hero-text{position:absolute;left:0;top:58px;width:430px;color:var(--white)}
.hero-text h1{font-size:43px;line-height:44px}
.hero-text p{margin-top:22px;font-size:13.5px;line-height:24px;opacity:.95}
.hero-actions{margin-top:24px;display:flex;gap:12px}
.hero-actions .btn{height:32px;line-height:32px;padding:0 24px}
.btn-ghost{border:1.5px solid var(--white);color:var(--white)}
.btn-white{background:var(--white);color:var(--blue)}
.hero-media{position:absolute;left:469px;top:67px;width:427px;height:285px;border-radius:10px;background:radial-gradient(circle at 35% 45%,#c13ef0 0%,#6a1a9a 35%,#2a0d3a 70%,#120812 100%);box-shadow:0 12px 30px rgba(0,0,0,.25)}

.notice{height:41px;background:var(--notice);color:var(--blue-dark);font-size:11px;display:flex;align-items:center;justify-content:center;gap:6px}

/* features */
.features{height:510px}
.section-title{font-size:26px;text-align:center}
.section-lead{text-align:center;color:var(--muted);font-size:13.5px;line-height:21px}
.features .section-title{padding-top:60px}
.features .section-lead{margin-top:16px}
.feature-grid{display:flex;gap:23px;margin-top:47px}
.feature-card{flex:1;height:177px;background:var(--card);border-radius:8px;text-align:center;padding-top:25px}
.icon-dot{width:47px;height:47px;border-radius:50%;background:var(--blue);margin:0 auto;display:flex;align-items:center;justify-content:center}
.feature-card h3{font-size:14.5px;margin-top:20px}
.feature-card p{font-size:11px;line-height:17px;color:var(--muted);margin:14px auto 0;width:235px}
.features .cta{margin-top:47px;text-align:center}

/* stats */
.stats{height:150px;background:var(--dark);color:var(--white)}
.stats .wrap{display:flex;height:150px;align-items:center}
.stat{flex:1;text-align:center}
.stat strong{display:block;font-family:"Arimo",sans-serif;font-size:24px;color:var(--sky-deep)}
.stat span{display:block;margin-top:6px;font-size:12.5px}

/* steps */
.steps{height:422px;background:var(--soft)}
.steps .section-title{padding-top:58px}
.steps .section-lead{margin-top:18px}
.step-grid{display:flex;gap:23px;margin-top:48px}
.step{flex:1;text-align:center}
.step-num{width:58px;height:58px;border-radius:50%;background:var(--blue);color:var(--white);font-family:"Arimo",sans-serif;font-weight:700;font-size:16px;line-height:58px;margin:0 auto}
.step h3{font-size:14.5px;margin-top:17px}
.step p{font-size:11px;line-height:17px;color:var(--muted);margin:14px auto 0;width:270px}

/* testimonials */
.reviews{height:445px}
.reviews .section-title{padding-top:58px}
.reviews .section-lead{margin-top:18px}
.review-grid{display:flex;gap:23px;margin-top:44px}
.review{flex:1;height:147px;background:var(--card);border-radius:8px;padding:24px 24px}
.reviewer{display:flex;align-items:center;gap:12px}
.avatar{width:34px;height:34px;border-radius:50%;background:linear-gradient(135deg,#c9ced4,#8a939c)}
.reviewer h4{font-size:12px}
.reviewer small{font-size:10px;color:var(--muted)}
.review blockquote{margin-top:12px;font-style:italic;font-size:11px;line-height:17px;color:#333}
.reviews .cta{margin-top:36px;text-align:center}

/* integrations */
.integrations{height:438px;background:var(--dark);color:var(--white)}
.integrations-text{position:absolute;left:0;top:66px;width:420px}
.integrations-text h2{font-size:26px;line-height:30px}
.integrations-text p{margin-top:14px;font-size:13.5px;line-height:20px;color:#e6e6e6}
.checklist{list-style:none;margin-top:20px}
.checklist li{display:flex;align-items:center;gap:10px;font-size:11px;margin-bottom:13px}
.integrations-text .btn{margin-top:10px;height:32px}
.integrations-media{position:absolute;left:469px;top:57px;width:427px;height:322px;border-radius:8px;background:linear-gradient(160deg,#4a6b3c 0%,#1b2a22 25%,#0d1a24 60%,#12324a 100%)}
.api-badge{position:absolute;left:451px;top:347px;background:var(--white);color:var(--ink);font-size:10.5px;border-radius:7px;padding:0 12px;height:36px;display:flex;align-items:center;gap:6px;box-shadow:0 4px 14px rgba(0,0,0,.25)}
.api-badge i{width:8px;height:8px;border-radius:50%;background:var(--green);display:block}

/* faq */
.faq{height:543px}
.faq .section-title{padding-top:55px}
.faq .section-lead{margin-top:18px}
.faq-grid{display:grid;grid-template-columns:1fr 1fr;gap:24px 24px;margin-top:42px}
.faq-item{height:109px;background:var(--white);border-radius:8px;box-shadow:0 2px 10px rgba(0,0,0,.06);padding:24px 23px}
.faq-item h3{font-size:13px}
.faq-item p{margin-top:12px;font-size:11px;line-height:17px;color:var(--muted)}
.faq .cta{margin-top:39px;text-align:center}

/* newsletter */
.newsletter{height:271px;background:var(--blue);color:var(--white);text-align:center}
.newsletter h2{font-size:26px;padding-top:58px}
.newsletter p{margin-top:14px;font-size:13px}
.subscribe{display:flex;justify-content:center;gap:12px;margin-top:26px}
.subscribe span.field{width:213px;height:29px;background:var(--white);border-radius:4px;color:#888;font-size:10.5px;text-align:left;padding-left:10px;line-height:29px}
.subscribe span.go{width:104px;height:29px;background:var(--white);color:var(--blue);border-radius:4px;font-size:10.5px;line-height:29px}
.newsletter small{display:block;margin-top:16px;font-size:9.5px;opacity:.85}

/* contact */
.contact{height:189px;background:#b6e2f8;text-align:center}
.contact h2{font-size:22px;padding-top:44px}
.contact-lines{display:flex;justify-content:center;gap:22px;margin-top:18px;font-size:11.5px;color:var(--blue-dark)}
.contact-lines span{display:flex;align-items:center;gap:6px}
.contact p{margin-top:18px;font-size:11.5px;color:#333}

/* footer */
.site-footer{height:249px;background:var(--dark);color:#bdbdbd}
.footer-cols{display:flex;padding-top:42px}
.footer-col{width:228px;font-size:11px}
.footer-col h4{color:var(--white);font-size:12px;font-family:"Cabin",sans-serif}
.footer-col ul{list-style:none;margin-top:14px}
.footer-col li{margin-bottom:9px}
.footer-about p{margin-top:14px;line-height:17px;width:170px}
.socials{display:flex;gap:12px;margin-top:8px}
.socials span{width:12px;height:12px;border:1.5px solid #9aa;border-radius:2px;display:block}
.footer-bottom{position:absolute;left:0;right:0;top:204px;display:flex;font-size:10px}
.footer-bottom nav{margin-left:auto;display:flex;gap:18px}
</style>
</head>
<body>

<header class="site-nav">
  <div class="wrap">
    <div class="brand">talvora.</div>
    <nav class="nav-links">
      <a href="#">Hem</a><a href="#">Funktioner</a><a href="#">Priser</a><a href="#">Recensioner</a><a href="#">FAQ</a><a href="#">Om oss</a><a href="#">Nyheter</a><a href="#">Kontakt</a>
    </nav>
    <a class="btn btn-solid nav-login" href="#">Logga in</a>
  </div>
</header>

<section class="hero">
  <div class="wrap">
    <div class="hero-text">
      <h1>Hantera dina kurser, deltagare och betalningar</h1>
      <p>Talvora är bokningsverktyget för dig som arrangerar kurser, utbildningar eller event. Med flexibla formulär, direktbetalning och automatiserad fakturering får du mer tid till det som verkligen räknas – innehållet.</p>
      <div class="hero-actions">
        <a class="btn btn-white" href="#">Prova gratis</a>
        <a class="btn btn-ghost" href="#">Boka demo</a>
      </div>
    </div>
    <div class="hero-media" role="img" aria-label="Eventlokal med lila och rosa scenljus"></div>
  </div>
</section>

<div class="notice">
  <svg width="12" height="12" viewBox="0 0 24 24" fill="none" stroke="currentColor" stroke-width="2"><path d="M9 18h6M10 22h4M12 2a7 7 0 0 0-4 12.7V17h8v-2.3A7 7 0 0 0 12 2z"/></svg>
  <span><b>Vi bygger om!</b> Just nu uppdaterar vi vår webbplats inför hösten. Under sommaren hittar du all viktig funktionalitet här.</span>
</div>

<section class="features">
  <div class="wrap">
    <h2 class="section-title">Hantera dina event, kurser och deltagare med full kontroll</h2>
    <p class="section-lead">Talvora, en del av Plomvik, erbjuder kraftfulla verktyg för arrangörer med över 15 års<br>erfarenhet av att hjälpa små föreningar till stora konferenser.</p>
    <div class="feature-grid">
      <div class="feature-card">
        <div class="icon-dot"><svg width="20" height="20" viewBox="0 0 24 24" fill="none" stroke="#fff" stroke-width="2"><path d="M14 2H6v20h12V6z M14 2v4h4 M9 12h6 M9 16h6"/></svg></div>
        <h3>Anpassningsbara formulär</h3>
        <p>Skapa flexibla anmälningsformulär som passar dina specifika behov och krav.</p>
      </div>
      <div class="feature-card">
        <div class="icon-dot"><svg width="20" height="20" viewBox="0 0 24 24" fill="none" stroke="#fff" stroke-width="2"><rect x="3" y="6" width="18" height="12" rx="2"/><path d="M3 10h18"/></svg></div>
        <h3>Direktbetalning</h3>
        <p>Ta emot betalningar direkt via kort eller Snabbpay med säker betalningshantering.</p>
      </div>
      <div class="feature-card">
        <div class="icon-dot"><svg width="20" height="20" viewBox="0 0 24 24" fill="none" stroke="#fff" stroke-width="2"><path d="M14 2H6v20h12V6z M14 2v4h4 M9 12h6 M9 16h6"/></svg></div>
        <h3>Automatiserad fakturering</h3>
        <p>Hantera fakturahantering med Faktora och spara tid på administration.</p>
      </div>
    </div>
    <div class="cta"><a class="btn btn-solid" href="#">Se alla funktioner</a></div>
  </div>
</section>

<section class="stats">
  <div class="wrap">
    <div class="stat"><strong>15+</strong><span>År av erfarenhet</span></div>
    <div class="stat"><strong>10k+</strong><span>Event hanterade</span></div>
    <div class="stat"><strong>99.9%</strong><span>Upptid</span></div>
  </div>
</section>

<section class="steps">
  <div class="wrap">
    <h2 class="section-title">Så här fungerar det</h2>
    <p class="section-lead">Kom igång på bara några minuter och hantera dina event professionellt från start till mål.</p>
    <div class="step-grid">
      <div class="step"><div class="step-num">1</div><h3>Skapa ditt event</h3><p>Använd våra flexibla formulär för att skapa anmälningssidor som passar dina behov perfekt.</p></div>
      <div class="step"><div class="step-num">2</div><h3>Ta emot anmälningar</h3><p>Deltagare anmäler sig enkelt via din hemsida eller våra färdiga mallar med direktbetalning.</p></div>
      <div class="step"><div class="step-num">3</div><h3>Hantera &amp; genomför</h3><p>Håll koll på deltagare, skicka kommunikation och hantera betalningar automatiskt.</p></div>
    </div>
  </div>
</section>

<section class="reviews">
  <div class="wrap">
    <h2 class="section-title">Våra kunder älskar Talvora</h2>
    <p class="section-lead">Över 1000+ organisationer använder Talvora för sina event och kurser.</p>
    <div class="review-grid">
      <article class="review">
        <div class="reviewer"><div class="avatar" role="img" aria-label="Profilbild"></div><div><h4>Anna Lindqvist</h4><small>Norrviks Högskola</small></div></div>
        <blockquote>"Talvora har revolutionerat hur vi hanterar våra kurser. Vi sparar timmar varje vecka!"</blockquote>
      </article>
      <article class="review">
        <div class="reviewer"><div class="avatar" role="img" aria-label="Profilbild"></div><div><h4>Erik Holmgren</h4><small>Nordkonferens AB</small></div></div>
        <blockquote>"Vi arrangerar stora konferenser och Talvora hanterar allt från 10 till 1000 deltagare utan problem."</blockquote>
      </article>
      <article class="review">
        <div class="reviewer"><div class="avatar" role="img" aria-label="Profilbild"></div><div><h4>Maria Sjöberg</h4><small>Västkustens Tennisklubb</small></div></div>
        <blockquote>"Som ideell förening uppskattar vi verkligen den kostnadsfria versionen."</blockquote>
      </article>
    </div>
    <div class="cta"><a class="btn btn-outline" href="#">Läs fler recensioner</a></div>
  </div>
</section>

<section class="integrations">
  <div class="wrap">
    <div class="integrations-text">
      <h2>Integrera med dina befintliga verktyg</h2>
      <p>Talvora fungerar sömlöst med din hemsida och andra system du redan använder.</p>
      <ul class="checklist">
        <li><svg width="15" height="15" viewBox="0 0 24 24" fill="none" stroke="#36b1ee" stroke-width="2.2"><circle cx="12" cy="12" r="10"/><path d="M7.5 12.5l3 3 6-6"/></svg>Embed-kod för din hemsida</li>
        <li><svg width="15" height="15" viewBox="0 0 24 24" fill="none" stroke="#36b1ee" stroke-width="2.2"><circle cx="12" cy="12" r="10"/><path d="M7.5 12.5l3 3 6-6"/></svg>REST API för avancerade integrationer</li>
        <li><svg width="15" height="15" viewBox="0 0 24 24" fill="none" stroke="#36b1ee" stroke-width="2.2"><circle cx="12" cy="12" r="10"/><path d="M7.5 12.5l3 3 6-6"/></svg>Webbly och Sitecraft plugins</li>
        <li><svg width="15" height="15" viewBox="0 0 24 24" fill="none" stroke="#36b1ee" stroke-width="2.2"><circle cx="12" cy="12" r="10"/><path d="M7.5 12.5l3 3 6-6"/></svg>Webhooks för realtidsuppdateringar</li>
      </ul>
      <a class="btn btn-solid" href="#">Utforska integrationer</a>
    </div>
    <div class="integrations-media" role="img" aria-label="Bärbar dator som visar en analyspanel med diagram"></div>
    <div class="api-badge"><i></i>API Connected</div>
  </div>
</section>

<section class="faq">
  <div class="wrap">
    <h2 class="section-title">Vanliga frågor</h2>
    <p class="section-lead">Svar på de mest frekventa frågorna från våra kunder.</p>
    <div class="faq-grid">
      <div class="faq-item"><h3>Hur kommer jag igång?</h3><p>Registrera dig för ett kostnadsfritt konto, skapa ditt första event och börja ta emot anmälningar direkt. Det tar bara några minuter.</p></div>
      <div class="faq-item"><h3>Vilka betalningsalternativ stöds?</h3><p>Vi stöder alla vanliga betalningsmetoder: kreditkort, Snabbpay, banköverföring och faktura. Alla betalningar hanteras säkert.</p></div>
      <div class="faq-item"><h3>Finns det begränsningar på antalet deltagare?</h3><p>I den kostnadsfria versionen kan du ha upp till 50 deltagare. Med Professional-planen finns inga begränsningar.</p></div>
      <div class="faq-item"><h3>Hur säker är deltagardatan?</h3><p>All data krypteras och vi följer GDPR-regelverket strikt. Våra servrar finns i Sverige med hög säkerhetsstandard.</p></div>
    </div>
    <div class="cta"><a class="btn btn-outline" href="#">Se alla vanliga frågor</a></div>
  </div>
</section>

<section class="newsletter">
  <h2>Håll dig uppdaterad</h2>
  <p>Få de senaste tipsen, funktionerna och branschinsikterna direkt i din inkorg.</p>
  <div class="subscribe"><span class="field">Din e-postadress</span><span class="go">Prenumerera</span></div>
  <small>Inget spam. Avregistrera dig när som helst.</small>
</section>

<section class="contact">
  <h2>Kontakta oss</h2>
  <div class="contact-lines">
    <span><svg width="13" height="13" viewBox="0 0 24 24" fill="none" stroke="currentColor" stroke-width="2"><path d="M22 16.9v3a2 2 0 0 1-2.2 2A19.8 19.8 0 0 1 2.1 4.2 2 2 0 0 1 4.1 2h3a2 2 0 0 1 2 1.7c.1 1 .4 1.9.7 2.8a2 2 0 0 1-.5 2.1L8 9.9a16 16 0 0 0 6 6l1.3-1.3a2 2 0 0 1 2.1-.4c.9.3 1.8.6 2.8.7a2 2 0 0 1 1.8 2z"/></svg>010-555 01 20</span>
    <span><svg width="13" height="13" viewBox="0 0 24 24" fill="none" stroke="currentColor" stroke-width="2"><rect x="2" y="4" width="20" height="16" rx="2"/><path d="M2 6l10 7 10-7"/></svg>support@talvora.se</span>
  </div>
  <p>Har du frågor eller vill veta mer? Vi finns här för att hjälpa dig!</p>
</section>

<footer class="site-footer">
  <div class="wrap">
    <div class="footer-cols">
      <div class="footer-col footer-about">
        <h4>talvora.</h4>
        <p>Professionell eventhantering för arrangörer i alla storlekar.</p>
        <div class="socials"><span></span><span></span><span></span></div>
      </div>
      <div class="footer-col"><h4>Produkt</h4><ul><li>Funktioner</li><li>Priser</li><li>API</li><li>Integrationer</li></ul></div>
      <div class="footer-col"><h4>Företag</h4><ul><li>Om oss</li><li>Nyheter</li><li>Karriär</li><li>Press</li></ul></div>
      <div class="footer-col"><h4>Support</h4><ul><li>FAQ</li><li>Kontakt</li><li>Hjälpcenter</li><li>System Status</li></ul></div>
    </div>
    <div class="footer-bottom">
      <span>© 2024 Talvora AB. Alla rättigheter förbehållna.</span>
      <nav><span>Integritetspolicy</span><span>Användarvillkor</span><span>GDPR</span></nav>
    </div>
  </div>
</footer>

</body>
</html>
```